We need to design Labels of one of Our Brand BrivaLune Lotion.

The purpose of this product is to keep mosquitoes away.
There are 3 variants of this lotion. So we need 3 designs for the product. These variants details are mentioned below:

1) Mosquito Repellent Lotion with Lavender Fragrance.
2) Mosquito Repellent Lotion with Natural Ingredients.
3) Mosquito Repellent Lotion for kids.

Kindly note the bottle will be WHITE for all the variants. Cap will of the bottle will be with accordance to the color of label. In the picture it is red just for presentation.

Kindly share design of Repellent Lotion with Lavendar Fragrance initially and if we give your positive feedback, then you may add further variants of the design.

The bottle shape is attached along with keylines. Also attaching logo. If there is any other option for logo, you can suggest which we would probably keep our existing logo.

Target Market(s)

B+, B, C+

Industry/Entity Type

Product

Colors
a54499
6b449b

Requirements
Must have
• Mosquito
• 100ml
Nice to have
• Purple color as background
Should not have
• Lavendar flower

```html
<!DOCTYPE html>
<html lang="en">
<head>
<meta charset="utf-8">
<title>BrivaLune Mosquito Repellent Lotion – Label Range</title>
<link rel="stylesheet" href="https://fonts.googleapis.com/css2?family=Lato:wght@400;700;900&display=swap">
<style>
  :root {
    --canvas-bg: #ffffff;
    --brand-blue: #1c6fc4;
    --banner-blue: #2f8fe0;
    --banner-light: #8fd0f7;
    --ink: #333a44;
    --lavender: #a54499;
    --lavender-deep: #7e2f7a;
    --natural: #5aa832;
    --natural-deep: #3e8a22;
    --kids: #3d72c4;
    --kids-deep: #24509b;
  }
  * { box-sizing: border-box; margin: 0; padding: 0; }
  html, body { width: 1200px; height: 1000px; overflow: hidden; background: var(--canvas-bg); }
  body { font-family: "Lato", sans-serif; color: var(--ink); position: relative; }

  .label {
    position: absolute;
    top: 400px;
    width: 300px;
    height: 470px;
    border-radius: 26px;
    overflow: hidden;
    background: linear-gradient(to bottom, #ffffff 0%, #ffffff 46%, var(--tint-soft) 66%, var(--tint) 100%);
    box-shadow: 0 0 0 1px #ececec;
  }
  .label--lavender { left: 108px; --tint: var(--lavender); --tint-deep: var(--lavender-deep); --tint-soft: #ecd3e8; }
  .label--natural  { left: 428px; --tint: var(--natural);  --tint-deep: var(--natural-deep);  --tint-soft: #d8ecc9; }
  .label--kids     { left: 748px; --tint: var(--kids);     --tint-deep: var(--kids-deep);     --tint-soft: #d2dff3; }

  .claim-banner { position: absolute; top: 0; left: 0; width: 300px; height: 110px; }
  .claim-icon { position: absolute; top: 50px; left: 26px; width: 28px; height: 28px; }
  .claim-text {
    position: absolute; top: 42px; left: 64px;
    color: #fff; font-size: 15px; line-height: 1.1; font-weight: 400; letter-spacing: 0.2px;
    transform: rotate(-9deg); transform-origin: left top;
    white-space: nowrap;
  }

  .brand {
    position: absolute; top: 146px; left: 0; width: 300px;
    display: flex; align-items: center; justify-content: center; gap: 10px;
  }
  .brand-dot { width: 26px; height: 26px; border-radius: 50%; background: var(--brand-blue); }
  .brand-name { font-size: 40px; font-weight: 900; color: var(--brand-blue); letter-spacing: -0.5px; }

  .product { position: absolute; top: 250px; left: 50px; width: 210px; }
  .product-title { font-size: 24px; font-weight: 900; color: var(--tint); line-height: 1; letter-spacing: 0.3px; }
  .product-type { font-size: 12px; font-weight: 900; color: var(--tint-deep); margin-top: 1px; padding-bottom: 4px; border-bottom: 1px solid var(--tint); }
  .product-variant { font-size: 11px; color: var(--ink); margin-top: 3px; }
  .product-variant--kids { margin-top: 10px; }
  .kids-word { font-size: 17px; font-weight: 900; letter-spacing: 1px; }
  .kids-word span:nth-child(1) { color: #3aa0e0; }
  .kids-word span:nth-child(2) { color: #e8453c; }
  .kids-word span:nth-child(3) { color: #f2b518; }
  .kids-word span:nth-child(4) { color: #49b048; }

  .benefits { position: absolute; top: 390px; left: 62px; font-size: 12px; line-height: 1.15; color: var(--ink); }
  .mosquito-mark {
    position: absolute; top: 378px; left: 170px; width: 38px; height: 38px;
    border-radius: 50%; background: radial-gradient(circle, #ffffff 55%, #d42a2a 58%);
  }
  .warning {
    position: absolute; top: 434px; left: 50px; width: 200px; height: 14px;
    background: var(--tint-deep); color: #fff; font-size: 7.5px; font-weight: 700;
    text-align: center; line-height: 12px; border: 1px solid #fff;
  }
  .volume { position: absolute; top: 451px; left: 0; width: 300px; text-align: center; color: #fff; font-size: 13px; }
</style>
</head>
<body>

<section class="label label--lavender">
  <svg class="claim-banner" viewBox="0 0 300 110" aria-hidden="true">
    <path d="M0 0 L300 0 L300 4 Q150 -4 0 26 Z" fill="var(--banner-light)"/>
    <path d="M0 26 Q150 -4 300 4 L300 62 Q150 48 0 102 Z" fill="var(--banner-blue)"/>
  </svg>
  <svg class="claim-icon" viewBox="0 0 28 28" aria-hidden="true">
    <circle cx="14" cy="14" r="12" fill="#fff"/>
    <path d="M8 14 L12.5 18.5 L20 10" stroke="var(--banner-blue)" stroke-width="2.6" fill="none"/>
  </svg>
  <p class="claim-text">DERMATOLOGICALLY<br>TESTED</p>
  <div class="brand"><span class="brand-dot"></span><span class="brand-name">BrivaLune</span></div>
  <div class="product">
    <h2 class="product-title">MOSQUITO</h2>
    <p class="product-type">REPELLENT LOTION</p>
    <p class="product-variant">with Lavender Fragrance</p>
  </div>
  <p class="benefits">Anti-Dengue<br>Hypoallergenic</p>
  <div class="mosquito-mark" role="img" aria-label="No-mosquito symbol"></div>
  <p class="warning">KEEP OUT OF REACH OF CHILDREN &amp; PETS</p>
  <p class="volume">100mL</p>
</section>

<section class="label label--natural">
  <svg class="claim-banner" viewBox="0 0 300 110" aria-hidden="true">
    <path d="M0 0 L300 0 L300 4 Q150 -4 0 26 Z" fill="var(--banner-light)"/>
    <path d="M0 26 Q150 -4 300 4 L300 62 Q150 48 0 102 Z" fill="var(--banner-blue)"/>
  </svg>
  <svg class="claim-icon" viewBox="0 0 28 28" aria-hidden="true">
    <circle cx="14" cy="14" r="12" fill="#fff"/>
    <path d="M8 14 L12.5 18.5 L20 10" stroke="var(--banner-blue)" stroke-width="2.6" fill="none"/>
  </svg>
  <p class="claim-text">DERMATOLOGICALLY<br>TESTED</p>
  <div class="brand"><span class="brand-dot"></span><span class="brand-name">BrivaLune</span></div>
  <div class="product">
    <h2 class="product-title">MOSQUITO</h2>
    <p class="product-type">REPELLENT LOTION</p>
    <p class="product-variant">with with Natural Ingredients</p>
  </div>
  <p class="benefits">Anti-Dengue<br>Hypoallergenic</p>
  <div class="mosquito-mark" role="img" aria-label="No-mosquito symbol"></div>
  <p class="warning">KEEP OUT OF REACH OF CHILDREN &amp; PETS</p>
  <p class="volume">100mL</p>
</section>

<section class="label label--kids">
  <svg class="claim-banner" viewBox="0 0 300 110" aria-hidden="true">
    <path d="M0 0 L300 0 L300 4 Q150 -4 0 26 Z" fill="var(--banner-light)"/>
    <path d="M0 26 Q150 -4 300 4 L300 62 Q150 48 0 102 Z" fill="var(--banner-blue)"/>
  </svg>
  <svg class="claim-icon" viewBox="0 0 28 28" aria-hidden="true">
    <circle cx="14" cy="14" r="12" fill="#fff"/>
    <path d="M8 14 L12.5 18.5 L20 10" stroke="var(--banner-blue)" stroke-width="2.6" fill="none"/>
  </svg>
  <p class="claim-text">DERMATOLOGICALLY<br>TESTED</p>
  <div class="brand"><span class="brand-dot"></span><span class="brand-name">BrivaLune</span></div>
  <div class="product">
    <h2 class="product-title">MOSQUITO</h2>
    <p class="product-type">REPELLENT LOTION</p>
    <p class="product-variant product-variant--kids">for <span class="kids-word"><span>K</span><span>I</span><span>D</span><span>S</span></span></p>
  </div>
  <p class="benefits">Anti-Dengue<br>Hypoallergenic</p>
  <div class="mosquito-mark" role="img" aria-label="No-mosquito symbol"></div>
  <p class="warning">KEEP OUT OF REACH OF CHILDREN &amp; PETS</p>
  <p class="volume">100mL</p>
</section>

</body>
</html>
```